Flyer für Kampfsport und Selbstverteidigung
Zielgruppe
Kampfsportschule für Kinder/Jugendliche und Erwachsene
Martial Arts Wenk
Flyerbeispiel finden Sie im Anhang
Aufgabenstellung
Es soll modern gestaltet sein und mit den Farben: Schwarz, Grau, weiß und rot gearbeitet werden.
Im Anhang ist mein alter Flyer. Der soll als Beispiel für Inhalt und Stil sein.

```html
<!DOCTYPE html>
<html lang="de">
<head>
<meta charset="utf-8">
<title>Martial Arts Wenk – Flyer</title>
<link href="https://fonts.googleapis.com/css2?family=Exo+2:ital,wght@1,800;1,900&family=Roboto+Condensed:wght@500;700&family=Russo+One&display=swap" rel="stylesheet">
<style>
:root{
  --page:#ececec;
  --black:#0d0d0d;
  --dark:#1b1b1b;
  --red:#d7141a;
  --red-deep:#8e0a0e;
  --grey:#595959;
  --grey-light:#cfcfcf;
  --white:#ffffff;
  --silver:#dcdcdc;
}
*{margin:0;padding:0;box-sizing:border-box}
html,body{width:1200px;height:896px;overflow:hidden;background:var(--page)}
.canvas{position:relative;width:1200px;height:896px}
.flyer{position:absolute;top:98px;width:499px;height:705px;background:var(--black);overflow:hidden;color:var(--white)}
.flyer--schedule{left:83px}
.flyer--info{left:625px}
.flyer-bg{position:absolute;inset:0}
.photo{position:absolute}
.brand{position:absolute;display:flex;align-items:center;gap:8px;font-family:"Russo One",sans-serif;color:var(--white);white-space:nowrap;z-index:2}
.brand-dot{width:22px;height:22px;border-radius:50%;background:var(--red)}
.headline{position:absolute;font-family:"Exo 2",sans-serif;font-weight:900;font-style:italic;text-transform:uppercase;color:var(--silver);line-height:1;text-align:center;text-shadow:0 2px 3px rgba(0,0,0,.6);white-space:nowrap;z-index:2}
/* schedule table */
.schedule{position:absolute;left:32px;top:374px;width:446px;border:2px solid var(--red);border-collapse:collapse;table-layout:fixed;font-family:"Roboto Condensed",sans-serif;font-weight:500}
.schedule th{height:41px;background:var(--black);font-size:11px;font-weight:700;color:var(--white);border-left:1px solid #444}
.schedule th.clock{background:var(--red);width:50px}
.schedule td{height:43.5px;font-size:13.5px;line-height:1.05;text-align:center;border:1px solid #3a3a3a;color:var(--white)}
.schedule td.time{background:var(--red);font-size:13.5px;border-color:var(--red)}
.kick{background:var(--dark)}
.jiu{background:var(--red)}
.trick{background:var(--grey)}
.ue25{background:var(--grey-light);color:#f4f4f4 !important}
.empty{background:#efefef}
.small{font-size:11.5px !important}
.contact-rule{position:absolute;display:flex;align-items:center;gap:10px;font-family:"Russo One",sans-serif;font-size:15px;color:var(--white)}
.contact-rule::before,.contact-rule::after{content:"";flex:1;height:1px;background:var(--white)}
.contact{position:absolute;display:flex;justify-content:space-between;font-family:"Russo One",sans-serif;font-size:16.5px;color:var(--white)}
.contact span{display:flex;align-items:center;gap:5px}
/* info flyer */
.tagline{position:absolute;left:0;width:100%;text-align:center;font-family:"Exo 2",sans-serif;font-weight:800;font-style:italic;color:var(--red);font-size:21px;line-height:1.05;text-transform:uppercase;z-index:2}
.tagline span{display:block}
.disciplines{position:absolute;left:24px;top:364px;z-index:2}
.disciplines h2{font-family:"Russo One",sans-serif;font-size:30px;line-height:1;color:var(--red);font-weight:400;margin-bottom:4px}
.disciplines li{list-style:none;font-family:"Russo One",sans-serif;font-size:19px;color:#111;line-height:27px;white-space:nowrap}
.disciplines li::before{content:"";display:inline-block;width:5px;height:5px;background:#111;margin:0 6px 4px 0}
.slogan{position:absolute;left:22px;top:564px;font-family:"Exo 2",sans-serif;font-weight:900;font-style:italic;font-size:24px;color:var(--white);z-index:2}
.lead{position:absolute;left:0;width:100%;text-align:center;font-family:"Russo One",sans-serif;color:var(--white)}
</style>
</head>
<body>
<main class="canvas">

  <section class="flyer flyer--schedule">
    <svg class="flyer-bg" width="499" height="705" viewBox="0 0 499 705">
      <defs>
        <linearGradient id="fadeWhite" x1="0" y1="0" x2="0" y2="1"><stop offset="0" stop-color="#fff"/><stop offset="1" stop-color="#fff" stop-opacity="0"/></linearGradient>
      </defs>
      <rect width="499" height="705" fill="#0d0d0d"/>
      <polygon points="0,0 120,0 200,60 60,300 0,260" fill="#b50f14"/>
      <polygon points="0,40 0,190 55,120" fill="url(#fadeWhite)" opacity=".7"/>
      <polygon points="330,0 499,0 499,150 400,220 310,60" fill="#c8161c"/>
      <polygon points="430,0 499,0 499,110 460,70" fill="#8e0a0e"/>
      <polygon points="499,140 499,240 440,180" fill="url(#fadeWhite)" opacity=".75"/>
      <polygon points="310,190 370,190 499,330 499,420 440,420" fill="#c8161c"/>
      <polygon points="450,430 499,420 499,560" fill="#9b0c10"/>
      <polygon points="40,260 140,230 110,340" fill="#5a0508" opacity=".8"/>
      <polygon points="380,705 499,600 499,705" fill="#c8161c"/>
    </svg>
    <div class="photo" role="img" aria-label="Foto: Mädchen im weißen Karateanzug mit gelbem Gürtel in Kampfhaltung" style="left:48px;top:82px;width:113px;height:288px;background:linear-gradient(180deg,#d9c2ae 0%,#f2f2f2 30%,#e6e6e6 65%,#d9c04a 72%,#e8e8e8 100%);border-radius:40px 40px 4px 4px"></div>
    <div class="brand" style="left:178px;top:115px;font-size:17px"><span class="brand-dot"></span>Martial Arts Wenk</div>
    <div class="headline" style="left:165px;top:256px;width:320px;font-size:33px;line-height:1.05">Martial Arts<br>Wenk</div>
    <div class="headline" style="left:150px;top:328px;width:340px;font-size:38px">Trainingsplan</div>

    <table class="schedule">
      <tr>
        <th class="clock"><svg width="24" height="24" viewBox="0 0 24 24" fill="none" stroke="#fff" stroke-width="2"><circle cx="12" cy="13" r="9"/><path d="M12 8v5l3 2M5 4l3-2M19 4l-3-2"/></svg></th>
        <th>MONTAG</th><th>DIENSTAG</th><th>MITTWOCH</th><th>DONNERSTAG</th><th>FREITAG</th>
      </tr>
      <tr>
        <td class="time">15:00<br>15:50</td>
        <td class="kick">Kick-Boxen<br>3-5 Jahre</td>
        <td class="jiu">Jiu-Jitsu<br>3-6 Jahre</td>
        <td class="kick">Kick-Boxen<br>3-5 Jahre</td>
        <td class="jiu">Jiu-Jitsu<br>3-6 Jahre</td>
        <td class="empty"></td>
      </tr>
      <tr>
        <td class="time">16:00<br>16:50</td>
        <td class="kick">Kick-Boxen<br>6-7 Jahre</td>
        <td class="jiu">Jiu-Jitsu<br>7-12 Jahre</td>
        <td class="kick">Kick-Boxen<br>6-7 Jahre</td>
        <td class="jiu">Jiu-Jitsu<br>7-12 Jahre</td>
        <td class="kick">Kick-Boxen<br>3-5 Jahre</td>
      </tr>
      <tr>
        <td class="time">17:00<br>18:50</td>
        <td class="kick">Kick-Boxen<br>8-10 Jahre</td>
        <td class="trick">Tricking<br>ab 6 Jahre</td>
        <td class="kick">Kick-Boxen<br>8-10 Jahre</td>
        <td class="trick">Tricking<br>ab 6 Jahre</td>
        <td class="kick small">Kick-Boxen<br>ab 7 Jahre<br>Ab Gelbgurt</td>
      </tr>
      <tr>
        <td class="time">18:15<br>19:15</td>
        <td class="kick">Kick-Boxen<br>10-12 Jahre</td>
        <td class="ue25">Kick-Boxen<br>Ü25 Gruppe</td>
        <td class="kick">Kick-Boxen<br>10-12 Jahre</td>
        <td class="ue25">Kick-Boxen<br>Ü25 Gruppe</td>
        <td class="ue25"></td>
      </tr>
      <tr>
        <td class="time">19:30<br>21:00</td>
        <td class="kick">Kick-Boxen<br>ab 13 Jahre</td>
        <td class="empty"></td>
        <td class="kick">Kick-Boxen<br>ab 13 Jahre</td>
        <td class="ue25"></td>
        <td class="ue25"></td>
      </tr>
    </table>

    <div class="contact-rule" style="left:31px;top:646px;width:449px">INFO &amp; PROBETRAINING:</div>
    <div class="contact" style="left:31px;top:668px;width:449px">
      <span><svg width="17" height="17" viewBox="0 0 24 24" fill="none" stroke="#d7141a" stroke-width="2.2"><circle cx="12" cy="12" r="9.5"/><path d="M8.5 7.5c0 4 3.5 8 8 8.5l1-2-2.5-1-1 1c-1.5-.6-2.8-1.9-3.4-3.4l1-1-1-2.5z"/></svg>0152 / 3608 7142</span>
      <span><svg width="20" height="15" viewBox="0 0 20 15" fill="none" stroke="#d7141a" stroke-width="1.8"><rect x="1" y="1" width="18" height="13"/><path d="M1 1l9 7 9-7"/></svg>info@martial-arts-wenk.de</span>
    </div>
  </section>

  <section class="flyer flyer--info">
    <svg class="flyer-bg" width="498" height="705" viewBox="0 0 498 705">
      <defs>
        <linearGradient id="topGlow" x1="0" y1="0" x2="0" y2="1"><stop offset="0" stop-color="#fff"/><stop offset=".55" stop-color="#9a9a9a"/><stop offset="1" stop-color="#1a1a1a"/></linearGradient>
        <linearGradient id="bandGrad" x1="0" y1="0" x2="1" y2="0"><stop offset="0" stop-color="#fff"/><stop offset=".6" stop-color="#ededed"/><stop offset="1" stop-color="#bdbdbd"/></linearGradient>
      </defs>
      <rect width="498" height="705" fill="#141414"/>
      <rect width="498" height="330" fill="url(#topGlow)"/>
      <polygon points="15,0 105,0 260,230 210,310" fill="#c8161c"/>
      <polygon points="480,0 395,0 240,230 290,310" fill="#c8161c"/>
      <polygon points="0,0 15,0 190,260 0,260" fill="#9b0c10" opacity=".55"/>
      <polygon points="498,0 480,0 305,260 498,260" fill="#9b0c10" opacity=".55"/>
      <polygon points="0,140 80,0 110,0 0,190" fill="#d7141a"/>
      <polygon points="498,140 420,0 390,0 498,190" fill="#d7141a"/>
      <rect y="260" width="498" height="90" fill="#1a1a1a"/>
      <polygon points="0,350 385,350 300,521 0,521" fill="url(#bandGrad)"/>
      <polygon points="385,350 498,350 498,521 300,521" fill="#b9b9b9"/>
      <polygon points="300,521 340,440 498,440 498,521" fill="#c8161c"/>
      <polygon points="98,535 139,535 118.5,561" fill="#d7141a"/>
      <rect y="597" width="498" height="3" fill="#d7141a"/>
    </svg>
    <div class="photo" role="img" aria-label="Foto: Lächelndes Mädchen im schwarzen Kampfsportshirt mit pinken Boxhandschuhen" style="left:388px;top:302px;width:110px;height:293px;background:linear-gradient(180deg,#b07a52 0%,#e2b59a 30%,#222 55%,#d0307a 70%,#1b1b1b 100%);border-radius:50px 50px 0 0"></div>
    <div class="brand" style="left:150px;top:78px;font-size:17px"><span class="brand-dot"></span>Martial Arts Wenk</div>
    <div class="headline" style="left:0;top:165px;width:498px;font-size:48px">Martial Arts</div>
    <div class="headline" style="left:0;top:212px;width:498px;font-size:66px">Wenk</div>
    <div class="tagline" style="top:284px"><span>Kampfsport</span><span>&amp; Selbstverteidigung</span></div>
    <div class="disciplines">
      <h2>DISZIPLINEN:</h2>
      <ul>
        <li>Kick-Boxen/Sportkarate</li>
        <li>Jiu-Jitsu Selbstverteidigung</li>
        <li>Tricking</li>
        <li>Ü25 Kick-Boxen</li>
      </ul>
    </div>
    <div class="slogan">Wir machen Kinder Stark!</div>
    <div class="lead" style="top:604px;font-size:16px"><span style="color:#8a8a8a">Leitung:</span> Daniel Wenk</div>
    <div class="lead" style="top:626px;font-size:13px">Am Sportpark 4 &nbsp;|&nbsp; 26409 Lindenhof</div>
    <div class="contact-rule" style="left:22px;top:650px;width:455px">INFO &amp; PROBETRAINING:</div>
    <div class="contact" style="left:22px;top:670px;width:455px">
      <span><svg width="17" height="17" viewBox="0 0 24 24" fill="none" stroke="#d7141a" stroke-width="2.2"><circle cx="12" cy="12" r="9.5"/><path d="M8.5 7.5c0 4 3.5 8 8 8.5l1-2-2.5-1-1 1c-1.5-.6-2.8-1.9-3.4-3.4l1-1-1-2.5z"/></svg>0152 / 3608 7142</span>
      <span><svg width="20" height="15" viewBox="0 0 20 15" fill="none" stroke="#d7141a" stroke-width="1.8"><rect x="1" y="1" width="18" height="13"/><path d="M1 1l9 7 9-7"/></svg>info@martial-arts-wenk.de</span>
    </div>
  </section>

</main>
</body>
</html>
```